IT Consulting Company needs a PowerPoint Template Design

We need a PowerPoint template design for an IT Consulting company called "Vorensik" (www.vorensik-example.com). We provide IT consulting services to customers. We mostly use the PowerPoint to present diagram, tables, lots of text. So, we would like to see the designs that is bold, modern and easy to read text. There should be the attached logo on every slides. The final design should communicate "Most Trusted IT Advisor".

Industry/Entity Type

It Company

Requirements
Must have
• The PowerPoint Template must have the following pages:
1. Title Slide (Main Title, Sub Title, Speaker, Date)
2. Title and Content (Bulleted content)
3. Title and Content (Numbered content)
4. Title and Table (Multiple columns with header and footer)
5. General Section header (Main Title, Sub Title)
6. Section header ("Demo" with graphic)
7. Section header ("Q&A" with graphic)
8. Section header ("Business Requirement" with graphic)
9. Section header ("Progress Update" with graphic)
10. Section header ("Project Plan" with graphic)
11. Closing Slide ("Thank you" with graphic)
Nice to have
• We prefer color blue. But other colors are welcome.

```html
<!DOCTYPE html>
<html lang="en">
<head>
<meta charset="utf-8">
<title>Vorensik – Presentation Template</title>
<link href="https://fonts.googleapis.com/css2?family=Ubuntu:wght@300;400;500;700&display=swap" rel="stylesheet">
<style>
:root{
  --navy:#2c4a6e;
  --navy-dark:#223a58;
  --footer:#1e2a38;
  --sky:#4d82ba;
  --red:#e3342c;
  --ink:#2a3f5c;
  --backdrop:#b9bdc3;
  --rule:#d8dde3;
  --tick:#4cae2f;
}
*{margin:0;padding:0;box-sizing:border-box}
html,body{width:804px;height:1200px;overflow:hidden;background:var(--backdrop)}
body{font-family:"Ubuntu",sans-serif;color:var(--ink)}
.sheet{position:absolute;left:0;top:0;width:910px;height:1358px;transform:scale(.88352);transform-origin:0 0}
.slide{position:absolute;width:438px;height:328px;background:#fff;overflow:hidden}
.col-a{left:14px}.col-b{left:459px}
.row-1{top:10px}.row-2{top:347px}.row-3{top:685px}.row-4{top:1022px}

/* wordmark */
.wordmark{font-weight:400;letter-spacing:1px;white-space:nowrap;display:inline-flex;align-items:center;gap:.12em}
.wordmark .dot{width:.18em;height:.18em;border-radius:50%;background:var(--red);display:inline-block}

/* cover */
.cover{background:linear-gradient(135deg,#fbfcfd,#eef1f5)}
.cover .wordmark{position:absolute;left:72px;top:122px;font-size:62px;color:var(--navy)}

/* title slide */
.hero-photo{position:absolute;inset:0;background:linear-gradient(120deg,#a9c4e2 0%,#d7e5f3 45%,#8fb0d6 100%)}
.title-box{position:absolute;left:0;top:141px;width:224px;height:157px;background:var(--navy)}
.title-box .wordmark{position:absolute;left:28px;top:34px;font-size:38px;color:#fff}
.title-box .title-band{position:absolute;left:0;bottom:0;width:100%;height:45px;background:var(--navy-dark);text-align:right;padding:12px 8px 0 0;color:#fff}
.title-band .main{font-size:9.5px;display:block}
.title-band .to{font-size:7px}
.hero-subtitle{position:absolute;left:231px;top:268px;color:#fff}
.hero-subtitle .big{font-size:30px;font-weight:300;display:block;line-height:1}
.hero-subtitle .speaker{font-size:9px;display:block;margin:2px 0 0 3px}
.hero-subtitle .date{font-size:6.5px;margin-left:3px}

/* content slide chrome */
.head{position:absolute;left:0;top:0;width:100%;height:45px;background:var(--navy);color:#fff}
.head h2{position:absolute;left:6px;top:9px;font-size:14.5px;font-weight:500;letter-spacing:.2px}
.head .sub{position:absolute;left:6px;top:25px;font-size:9px;font-weight:300}
.head .tag{position:absolute;right:12px;top:8px;font-size:19px;font-weight:300;text-align:right;line-height:1}
.head .tag small{display:block;font-size:6px;margin-top:2px;text-align:left;padding-left:1px}
.foot{position:absolute;left:0;bottom:0;width:100%;height:21px;background:var(--footer);color:#fff;font-size:6.5px;display:flex;align-items:center}
.foot .num{width:30px;padding-left:10px;font-weight:700}
.foot .wordmark{font-size:11px;color:#fff;letter-spacing:.5px}
.foot .to{margin-left:6px}

/* numbered list */
.req-list{position:absolute;left:20px;top:62px;width:392px;font-size:6.6px;line-height:1.38;color:var(--ink);padding-left:10px}
.req-list li{margin-bottom:9.6px;text-align:justify}
.req-list b{font-weight:700}

/* Q&A */
.qa{position:absolute;left:26px;width:370px}
.qa .q{font-size:6.3px;font-style:italic;line-height:1.3;padding-left:10px;position:relative;width:290px}
.qa .q::before,.qa .a::before{content:"";position:absolute;left:0;top:2px;width:0;height:0;border-left:4px solid var(--red);border-top:2.5px solid transparent;border-bottom:2.5px solid transparent}
.qa .a{position:relative;margin:5px 0 0 44px;background:var(--navy);color:#fff;border-radius:3px;font-size:6.3px;font-style:italic;line-height:1.3;padding:4px 6px 4px 16px}
.qa .a::before{left:5px;top:5px;border:none;width:5px;height:2px;background:var(--red)}
.qa .a::after{content:"";position:absolute;left:150px;top:-5px;border-bottom:5px solid var(--navy);border-left:5px solid transparent;border-right:5px solid transparent}

/* progress */
.phase{position:absolute;top:95px;width:93px;height:110px;background:var(--navy);border-radius:3px;color:#fff;padding:6px 10px}
.phase.current{background:var(--sky)}
.phase h3{font-size:9.5px;font-weight:500;line-height:1.15;margin-bottom:2px}
.phase li{list-style:none;font-size:6.6px;line-height:1.35;position:relative;padding-left:8px}
.phase li::before{content:"";position:absolute;left:0;top:2px;border-left:4px solid var(--red);border-top:2.5px solid transparent;border-bottom:2.5px solid transparent}
.timeline{position:absolute;left:14px;top:225px;width:412px;height:20px}
.timeline span{position:absolute;top:0;font-size:8.5px;color:var(--sky);width:100px;text-align:center}

/* demo */
.step-title{position:absolute;top:85px;font-size:12px;color:var(--navy);font-weight:500}
.step-title span{font-weight:300}
.step-shot{position:absolute;top:105px;width:113px;height:133px;background:linear-gradient(180deg,#2f5079,#1f2d40)}
.step-shot svg{position:absolute;left:25px;top:37px}
.step-text{position:absolute;top:245px;width:113px;font-size:5.7px;line-height:1.45;color:#4a5a70;padding-left:9px;text-align:justify}
.step-text::before{content:"";position:absolute;left:0;top:2px;border-left:4px solid var(--red);border-top:2.5px solid transparent;border-bottom:2.5px solid transparent}
.step-link{position:absolute;top:171px;width:24px;border-top:1px dotted #556}

/* table */
.plan{position:absolute;left:15px;top:55px;width:406px;border-collapse:collapse;font-size:5px;color:#555}
.plan th{background:var(--footer);color:#fff;font-size:6.8px;font-weight:500;height:20px;border-right:1px solid #fff}
.plan td{height:21.8px;border-bottom:1px solid var(--rule);text-align:center;background:#f7f8fa}
.plan tr:nth-child(even) td{background:#fff}
.plan td.step{text-align:left;padding-left:4px;line-height:1.25}
.plan td.resp{text-align:left;padding-left:4px}
.plan td.idx{color:var(--ink);font-size:6.5px}
.plan tfoot td{background:#e7e9ec;font-size:7px;height:18px;color:#555}

/* closing */
.closing{background:linear-gradient(160deg,#2f5079,#28466b)}
.closing .wordmark{position:absolute;left:52px;top:126px;font-size:66px;color:#fff}
.closing .thanks{position:absolute;left:0;width:100%;top:202px;text-align:center;color:#fff;font-size:12px;letter-spacing:2px}
.contact{position:absolute;left:11px;top:253px;color:#fff;font-size:5.6px;line-height:1.35}
.contact b{font-size:6.8px;display:block;margin-bottom:1px}
.contact .office{margin-top:9px}
.site{position:absolute;right:63px;bottom:12px;color:#fff;font-size:6.8px}
.social{position:absolute;right:12px;bottom:8px;display:flex;gap:7px}
.social i{width:13px;height:13px;background:#fff;border-radius:2px;display:block}
</style>
</head>
<body>
<div class="sheet">

  <!-- cover -->
  <section class="slide col-a row-1 cover">
    <div class="wordmark">Vorensik<i class="dot"></i></div>
  </section>

  <!-- title slide -->
  <section class="slide col-b row-1">
    <div class="hero-photo" role="img" aria-label="Photo of a hand in a light blue shirt tapping a tablet"></div>
    <div class="title-box">
      <div class="wordmark">Vorensik</div>
      <div class="title-band">
        <span class="main">Main Title of Presentation</span>
        <span class="to">to <b>Client</b>/Customer</span>
      </div>
    </div>
    <div class="hero-subtitle">
      <span class="big">Subtitle.</span>
      <span class="speaker">Name of Speaker</span>
      <span class="date">June 2013</span>
    </div>
  </section>

  <!-- business requirement -->
  <section class="slide col-a row-2">
    <header class="head"><h2>BUSINESS REQUIREMENT</h2><div class="sub">Requirement Subtitle</div><div class="tag">Subtitle.<small>June 2013</small></div></header>
    <ol class="req-list">
      <li><b>Aenean</b> ridiculus tortor quis interdum id habitant ad, natoque consectetuer nisl auctor libero quisque euismod ante inceptos malesuada ligula mattis.</li>
      <li>Nulla, netus pulvinar pellentesque porttitor purus maecenas tellus hac nulla lacus. Lorem. Nostra laoreet nulla, dis cursus nascetur dolor odio Eu Magna molestie montes dui mus cursus habitasse mauris tempor.</li>
      <li>Varius inceptos <b>nascetur</b> mollis dui aptent ultrices. Pretium pulvinar ante lobortis convallis lectus netus vitae penatibus eros at blandit. Parturient.</li>
      <li><b>Aenean</b> ridiculus tortor quis interdum id habitant ad, natoque consectetuer nisl auctor libero quisque euismod ante inceptos malesuada ligula mattis.</li>
      <li>Nulla, netus pulvinar pellentesque porttitor purus maecenas tellus hac nulla lacus. Lorem. Nostra laoreet nulla, dis cursus nascetur dolor odio Eu Magna molestie montes dui mus cursus habitasse mauris tempor.</li>
      <li>Varius inceptos <b>nascetur</b> mollis dui aptent ultrices. Pretium pulvinar ante lobortis convallis lectus netus vitae penatibus eros at blandit. Parturient.</li>
      <li>Nulla, netus pulvinar pellentesque porttitor purus maecenas tellus hac nulla lacus. Lorem. Nostra laoreet nulla, dis cursus nascetur dolor odio Eu Magna molestie montes dui mus cursus habitasse mauris tempor.</li>
      <li>Varius inceptos <b>nascetur</b> mollis dui aptent ultrices. Pretium pulvinar ante lobortis convallis lectus netus vitae penatibus eros at blandit. Parturient.</li>
    </ol>
    <footer class="foot"><span class="num">5</span><span class="wordmark">Vorensik</span><span class="to">| To <b>Client</b>/Customer</span></footer>
  </section>

  <!-- Q&A -->
  <section class="slide col-b row-2">
    <header class="head"><h2>QUESTIONS &amp; ANSWERS</h2><div class="sub">Q&amp;A Subtitle</div><div class="tag">Subtitle.<small>June 2013</small></div></header>
    <div class="qa" style="top:58px"><p class="q"><b>"Aenean</b> ridiculus tortor quis interdum id habitant ad, natoque consectetuer nisl auctor libero quisque euismod ante inceptos malesuada ligula mattis?"</p><p class="a"><b>"Aenean</b> ridiculus tortor quis interdum id habitant ad, natoque consectetuer nisl auctor libero quisque euismod ante inceptos malesuada ligula mattis?"</p></div>
    <div class="qa" style="top:122px"><p class="q"><b>"Aenean</b> ridiculus tortor quis interdum id habitant ad, natoque consectetuer nisl auctor libero quisque euismod ante inceptos malesuada ligula mattis?"</p><p class="a"><b>"Aenean</b> ridiculus tortor quis interdum id habitant ad, natoque consectetuer nisl auctor libero quisque euismod ante inceptos malesuada ligula mattis?"</p></div>
    <div class="qa" style="top:186px"><p class="q"><b>"Aenean</b> ridiculus tortor quis interdum id habitant ad, natoque consectetuer nisl auctor libero quisque euismod ante inceptos malesuada ligula mattis?"</p><p class="a"><b>"Aenean</b> ridiculus tortor quis interdum id habitant ad, natoque consectetuer nisl auctor libero quisque euismod ante inceptos malesuada ligula mattis?"</p></div>
    <div class="qa" style="top:250px"><p class="q"><b>"Aenean</b> ridiculus tortor quis interdum id habitant ad, natoque consectetuer nisl auctor libero quisque euismod ante inceptos malesuada ligula mattis?"</p><p class="a"><b>"Aenean</b> ridiculus tortor quis interdum id habitant ad, natoque consectetuer nisl auctor libero quisque euismod ante inceptos malesuada ligula mattis?"</p></div>
    <footer class="foot"><span class="num">4</span><span class="wordmark">Vorensik</span><span class="to">| To <b>Client</b>/Customer</span></footer>
  </section>

  <!-- progress update -->
  <section class="slide col-a row-3">
    <header class="head"><h2>PROGRESS UPDATE</h2><div class="sub">Update Subtitle</div><div class="tag">Subtitle.<small>June 2013</small></div></header>
    <div class="phase" style="left:14px"><h3>Requirements and Design</h3><ul><li>Working Sessions to define:</li><li>Functionality Requirements</li><li>Data Requirements</li><li>Reporting Requirements</li></ul></div>
    <div class="phase" style="left:119px"><h3>Build Sprints</h3><ul><li>Data fields</li><li>Functionality Configuration</li><li>Report Buildout</li><li>Test System</li><li>End User Review</li></ul></div>
    <div class="phase current" style="left:224px"><h3>Application Readiness</h3><ul><li>Data Loading</li><li>Final Application Review</li><li>Training</li><li>End-user Training</li><li>Administrator Training</li></ul></div>
    <div class="phase" style="left:329px"><h3>System Launch</h3><ul><li>Initial Rollout Support</li></ul></div>
    <div class="timeline">
      <svg width="412" height="20" style="position:absolute;left:0;top:0">
        <line x1="2" y1="16" x2="404" y2="16" stroke="#2c4a6e" stroke-width="1" stroke-dasharray="2 2"/>
        <path d="M404 13 L410 16 L404 19Z" fill="#2c4a6e"/>
        <line x1="2" y1="9" x2="2" y2="20" stroke="#2c4a6e"/>
        <line x1="99" y1="9" x2="99" y2="20" stroke="#2c4a6e"/>
        <line x1="204" y1="9" x2="204" y2="20" stroke="#2c4a6e"/>
        <line x1="309" y1="9" x2="309" y2="20" stroke="#2c4a6e"/>
        <line x1="26" y1="11" x2="72" y2="11" stroke="#4d82ba" stroke-width=".6"/>
      </svg>
      <span style="left:0">2-3 Days</span><span style="left:102px">2-3 weeks</span><span style="left:205px">1 month</span><span style="left:310px">2 months</span>
    </div>
    <footer class="foot"><span class="num">6</span><span class="wordmark">Vorensik</span><span class="to">| To <b>Client</b>/Customer</span></footer>
  </section>

  <!-- demonstration -->
  <section class="slide col-b row-3">
    <header class="head"><h2>DEMONSTRATION</h2><div class="sub">Demo Subtitle</div><div class="tag">Subtitle.<small>June 2013</small></div></header>
    <div class="step-title" style="left:29px">Step <span>1</span></div>
    <div class="step-title" style="left:164px">Step <span>2</span></div>
    <div class="step-title" style="left:299px">Step <span>3</span></div>
    <div class="step-shot" style="left:27px" role="img" aria-label="Screenshot placeholder for demo step 1"><svg width="62" height="58" viewBox="0 0 62 58"><rect x="1" y="1" width="60" height="56" fill="none" stroke="#8fa4bf" stroke-width="2"/><path d="M6 50 L24 22 L36 40 L42 32 L56 50Z" fill="#8fa4bf"/><circle cx="45" cy="15" r="5" fill="#8fa4bf"/></svg></div>
    <div class="step-shot" style="left:163px" role="img" aria-label="Screenshot placeholder for demo step 2"><svg width="62" height="58" viewBox="0 0 62 58"><rect x="1" y="1" width="60" height="56" fill="none" stroke="#8fa4bf" stroke-width="2"/><path d="M6 50 L24 22 L36 40 L42 32 L56 50Z" fill="#8fa4bf"/><circle cx="45" cy="15" r="5" fill="#8fa4bf"/></svg></div>
    <div class="step-shot" style="left:299px" role="img" aria-label="Screenshot placeholder for demo step 3"><svg width="62" height="58" viewBox="0 0 62 58"><rect x="1" y="1" width="60" height="56" fill="none" stroke="#8fa4bf" stroke-width="2"/><path d="M6 50 L24 22 L36 40 L42 32 L56 50Z" fill="#8fa4bf"/><circle cx="45" cy="15" r="5" fill="#8fa4bf"/></svg></div>
    <div class="step-link" style="left:140px"></div><div class="step-link" style="left:275px"></div>
    <p class="step-text" style="left:22px"><b>Aenean</b> ridiculus tortor quis interdum id habitant ad, natoque consectetuer nisl auctor libero quisque euismod ante inceptos malesuada ligula mattis.</p>
    <p class="step-text" style="left:157px"><b>Aenean</b> ridiculus tortor quis interdum id habitant ad, natoque consectetuer nisl auctor libero quisque euismod ante inceptos malesuada ligula mattis.</p>
    <p class="step-text" style="left:294px"><b>Aenean</b> ridiculus tortor quis interdum id habitant ad, natoque consectetuer nisl auctor libero quisque euismod ante inceptos malesuada ligula mattis.</p>
    <footer class="foot"><span class="num">3</span><span class="wordmark">Vorensik</span><span class="to">| To <b>Client</b>/Customer</span></footer>
  </section>

  <!-- project plan -->
  <section class="slide col-a row-4">
    <header class="head"><h2>PROJECT PLAN</h2><div class="sub">Plan Subtitle</div><div class="tag">Subtitle.<small>June 2013</small></div></header>
    <table class="plan">
      <thead><tr><th style="width:40px">Item</th><th style="width:112px">Step/Action</th><th style="width:73px">Responsible</th><th style="width:72px">Target Date</th><th style="width:72px">Actual Date</th><th>Go/No Go</th></tr></thead>
      <tbody>
        <tr><td class="idx">1</td><td class="step">Introductions and understand Business X, Y, Z high level needs</td><td class="resp">Business X, Y, Z</td><td>5/24/2013</td><td>5/24/2013</td><td><svg width="16" height="14" viewBox="0 0 16 14"><path d="M1 7 L6 12 L15 1" fill="none" stroke="#4cae2f" stroke-width="3"/></svg></td></tr>
        <tr><td class="idx">2</td><td class="step">Understand current situation and safety management project needs with Business X, Y, Z</td><td class="resp">Business X, Y, Z</td><td>5/31/2013</td><td>5/31/2013</td><td><svg width="16" height="14" viewBox="0 0 16 14"><path d="M1 7 L6 12 L15 1" fill="none" stroke="#4cae2f" stroke-width="3"/></svg></td></tr>
        <tr><td class="idx">3</td><td class="step">Submit Proposal</td><td class="resp">Vorensik</td><td>6/3/2013</td><td>6/3/2013</td><td><svg width="16" height="14" viewBox="0 0 16 14"><path d="M1 7 L6 12 L15 1" fill="none" stroke="#4cae2f" stroke-width="3"/></svg></td></tr>
        <tr><td class="idx">4</td><td class="step">Review Proposal</td><td class="resp">Business X, Y, Z</td><td>TBD</td><td>TBD</td><td></td></tr>
        <tr><td class="idx">5</td><td class="step">Prepare Final Proposal &amp; Statement of Work (SOW)</td><td class="resp">Vorensik</td><td>TBD</td><td>TBD</td><td></td></tr>
        <tr><td class="idx">6</td><td class="step">Complete and sign SOW</td><td class="resp">Business X, Y, Z</td><td>TBD</td><td>TBD</td><td></td></tr>
        <tr><td class="idx">7</td><td class="step">Schedule project start date</td><td class="resp">Business X, Y, Z</td><td>TBD</td><td>TBD</td><td></td></tr>
        <tr><td class="idx" style="color:#e3342c">8</td><td class="step">Kick-off Project</td><td class="resp">Vorensik</td><td>TBD</td><td>TBD</td><td></td></tr>
        <tr><td class="idx">9</td><td class="step">Complete Project</td><td class="resp">Vorensik</td><td>TBD</td><td>TBD</td><td></td></tr>
      </tbody>
      <tfoot><tr><td colspan="6">Other Information</td></tr></tfoot>
    </table>
    <footer class="foot"><span class="num">7</span><span class="wordmark">Vorensik</span><span class="to">| To <b>Client</b>/Customer</span></footer>
  </section>

  <!-- closing -->
  <section class="slide col-b row-4 closing">
    <div class="wordmark">Vorensik<i class="dot"></i></div>
    <p class="thanks">Thank you</p>
    <div class="contact">
      <b>Contact us:</b>
      02-555-0142<br>info@vorensik-example.com
      <div class="office"><b>Main Office</b>18/4 Example Lane, River-<br>side District, Sample<br>City 10000</div>
    </div>
    <div class="site">www.vorensik-example.com</div>
    <div class="social"><i></i><i></i><i></i></div>
  </section>

</div>
</body>
</html>
```